Letterhead Design Project

I am the new owner of an existing Accouting and Financial Planning Firm (which I have been an employee at for 3 years)
We need to change the letterhead due to a change to the company's ABN etc., so thought we would like to modernise this at the same time.
We wish to keep the existing logo so there is familiarity to the clients. As per the notes on the attached document, we are happy to remove the wording from the logo, whichever will look better.
The letterhead needs to be professional, yet modern.
I will upload our logo and the required details for the letterhead.

Industry/Entity Type

Financial

Requirements
Must have
• Logo and provided business details.

```html
<!DOCTYPE html>
<html lang="en">
<head>
<meta charset="utf-8">
<title>Harlow Accountants – Letterhead</title>
<link href="https://fonts.googleapis.com/css2?family=Source+Sans+3:wght@400;600;700&display=swap" rel="stylesheet">
<style>
  :root {
    --backdrop: #e4e4e4;
    --paper: #ffffff;
    --navy: #163e7a;
    --orange: #f39a1e;
    --wave-warm: #f7c88a;
    --wave-cool: #a9c6ec;
  }
  * { box-sizing: border-box; margin: 0; padding: 0; }
  html, body {
    width: 1200px;
    height: 907px;
    overflow: hidden;
    background: var(--backdrop);
    font-family: "Source Sans 3", "Myriad Pro", sans-serif;
  }
  .canvas {
    position: relative;
    width: 1200px;
    height: 907px;
  }
  .letterhead {
    position: absolute;
    left: 313px;
    top: 42px;
    width: 576px;
    height: 818px;
    background: var(--paper);
    overflow: hidden;
  }
  .wave-area {
    position: absolute;
    inset: 0;
    width: 576px;
    height: 818px;
  }
  .brand {
    position: absolute;
    top: 86px;
    right: 40px;
    display: flex;
    align-items: flex-end;
    gap: 5px;
    font-weight: 700;
    font-size: 34px;
    line-height: 1;
    color: var(--navy);
    letter-spacing: -0.5px;
  }
  .brand-mark {
    width: 9px;
    height: 9px;
    margin-bottom: 5px;
    background: var(--orange);
  }
  .footer {
    position: absolute;
    left: 31px;
    top: 745px;
    display: flex;
    gap: 8px;
  }
  .footer-mark {
    width: 8px;
    height: 8px;
    margin-top: 2px;
    background: var(--orange);
    flex: none;
  }
  .footer-details {
    font-style: normal;
    font-size: 7.8px;
    line-height: 10.5px;
    font-weight: 600;
    color: var(--navy);
    white-space: nowrap;
  }
  .footer-details .web { color: var(--orange); font-weight: 400; }
</style>
</head>
<body>
<main class="canvas">
  <section class="letterhead">
    <svg class="wave-area" viewBox="0 0 576 818">
      <defs>
        <linearGradient id="warmFade" x1="0" y1="0" x2="1" y2="0">
          <stop offset="0" stop-color="var(--wave-warm)" stop-opacity="0.55"/>
          <stop offset="0.6" stop-color="var(--wave-warm)" stop-opacity="0.25"/>
          <stop offset="1" stop-color="var(--wave-warm)" stop-opacity="0"/>
        </linearGradient>
        <linearGradient id="coolFade" x1="1" y1="0" x2="0" y2="0">
          <stop offset="0" stop-color="var(--wave-cool)" stop-opacity="0.55"/>
          <stop offset="0.6" stop-color="var(--wave-cool)" stop-opacity="0.22"/>
          <stop offset="1" stop-color="var(--wave-cool)" stop-opacity="0"/>
        </linearGradient>
      </defs>
      <path class="wave-top" role="img" aria-label="Soft warm orange wave decoration"
            fill="url(#warmFade)"
            d="M0,0 H470 C330,10 150,60 0,245 Z"/>
      <path class="wave-bottom" role="img" aria-label="Soft light blue wave decoration"
            fill="url(#coolFade)"
            d="M576,596 C480,650 300,680 110,688 C300,694 470,720 576,770 Z"/>
    </svg>

    <div class="brand">
      <span class="brand-name">Harlow</span>
      <span class="brand-mark"></span>
    </div>

    <footer class="footer">
      <span class="footer-mark"></span>
      <address class="footer-details">
        Harlow Accountants &amp; Financial Services; ABN: 48 207 316 592<br>
        12 Kestrel Road, Marlow Vale, Vic, 3712; PO Box 318, Ferndale, NSW, 2655<br>
        Ph: 02 5550 1482 Fax: 02 5550 2736; Email: office@harlowaccountants.com.au<br>
        <span class="web">www.harlowaccountants.com.au</span>
      </address>
    </footer>
  </section>
</main>
</body>
</html>
```